Yard Sign Design Needed

Yard sign needed for mowing & landscaping company. Would like to use the top logo with black background which is attached. Would like MOWING to be in large standout letters. The word "landscaping" can be smaller and more artistic or omitted. Will need room for phone number once design is approved. The phone number will need to stand out and look identical/similar to the word 'MOWING"

```html
<!DOCTYPE html>
<html lang="en">
<head>
<meta charset="utf-8">
<title>Talvern Contractors – Mowing Yard Sign</title>
<link rel="stylesheet" href="https://fonts.googleapis.com/css2?family=Oswald:wght@500;700&family=Pinyon+Script&display=swap">
<style>
  :root {
    --page-bg: #ffffff;
    --sign-black: #000000;
    --leaf-green: #8cb43a;
    --text-white: #ffffff;
  }
  * { margin: 0; padding: 0; box-sizing: border-box; }
  html, body {
    width: 1200px;
    height: 549px;
    overflow: hidden;
    background: var(--page-bg);
  }
  .canvas {
    position: relative;
    width: 1200px;
    height: 549px;
  }
  .yard-sign {
    position: absolute;
    left: 430px;
    top: 20px;
    width: 340px;
    height: 509px;
    background: var(--sign-black);
    overflow: hidden;
    box-shadow: 0 2px 6px rgba(0,0,0,0.25);
  }
  .corner-accents {
    position: absolute;
    inset: 0;
    width: 100%;
    height: 100%;
  }
  .corner-accents polygon { fill: var(--leaf-green); }
  .brand-mark {
    position: absolute;
    left: 50%;
    top: 62px;
    width: 62px;
    height: 62px;
    margin-left: -31px;
    background: var(--leaf-green);
  }
  .brand-name {
    position: absolute;
    left: 0;
    right: 0;
    top: 160px;
    text-align: center;
    font-family: "Oswald", sans-serif;
    font-weight: 500;
    color: var(--leaf-green);
    text-transform: uppercase;
    line-height: 1;
  }
  .brand-name .brand-primary {
    display: block;
    font-size: 44px;
    letter-spacing: 4px;
  }
  .brand-name .brand-secondary {
    display: block;
    margin-top: 8px;
    font-size: 17px;
    letter-spacing: 3px;
  }
  .service-headline {
    position: absolute;
    left: 0;
    right: 0;
    top: 270px;
    text-align: center;
    font-family: "Oswald", sans-serif;
    font-weight: 700;
    font-size: 84px;
    line-height: 1;
    letter-spacing: 2px;
    color: var(--text-white);
  }
  .service-subline {
    position: absolute;
    left: 0;
    right: 0;
    top: 338px;
    text-align: center;
    font-family: "Pinyon Script", cursive;
    font-size: 52px;
    line-height: 1;
    color: var(--leaf-green);
  }
  .phone-number {
    position: absolute;
    left: 0;
    right: 0;
    top: 412px;
    text-align: center;
    font-family: "Oswald", sans-serif;
    font-weight: 700;
    font-size: 46px;
    line-height: 1;
    letter-spacing: 1px;
    color: var(--text-white);
  }
</style>
</head>
<body>
  <main class="canvas">
    <section class="yard-sign">
      <svg class="corner-accents" viewBox="0 0 340 509" preserveAspectRatio="none" aria-hidden="true">
        <polygon points="0,0 67,0 0,73"/>
        <polygon points="340,0 273,0 340,73"/>
        <polygon points="0,509 67,509 0,440"/>
        <polygon points="340,509 273,509 340,440"/>
      </svg>
      <div class="brand-mark" aria-hidden="true"></div>
      <h1 class="brand-name">
        <span class="brand-primary">Talvern</span>
        <span class="brand-secondary">Contractors LLC</span>
      </h1>
      <p class="service-headline">MOWING</p>
      <p class="service-subline">landscaping</p>
      <p class="phone-number">00 987 654 32</p>
    </section>
  </main>
</body>
</html>
```